Postcard Design

We are a pet resort located near Atlanta's Pembrook Calloway Airport. I want a postcard that will show dogs playing and the offer will be "New customers receive 50% off boarding" *
* 50% offer applies to standard lodging fees only. Amenities and playtimes not included in this offer. Valid for up to 10 nights of boarding. Blackout dates of July 4th, Thanksgiving week and Christmas week apply. Reservations required.
The backside of the postcard will read, "New daycare customers recieve ONE WEEK of FREE daycare for your dog".*
* offer good for 5 consecutive days of daycare only-not in conjuction with overnight lodging. Good for one pet per family only. Offer not valid on July 4th week, Thanksgiving week or Christmas week.

```html
<!DOCTYPE html>
<html lang="en">
<head>
<meta charset="utf-8">
<title>Pet Resort Postcard – Boarding Offer</title>
<link href="https://fonts.googleapis.com/css2?family=Roboto+Condensed:wght@400;700&family=Roboto:wght@400;700&family=Allura&family=Marcellus&display=swap" rel="stylesheet">
<style>
  :root {
    --brand-red: #d1121b;
    --deep-red: #a60a10;
    --text-red: #b3141c;
    --gold-light: #e9d98a;
    --gold-mid: #c9ad62;
    --gold-dark: #a88a4a;
    --silver: #d9d9d9;
    --white: #ffffff;
    --park-green: #6aa632;
    --park-shade: #3b4a22;
    --autumn: #c98a35;
  }
  html, body {
    margin: 0;
    padding: 0;
    width: 1200px;
    height: 923px;
    overflow: hidden;
    background: #ffffff;
  }
  .postcard {
    position: relative;
    width: 1200px;
    height: 923px;
    overflow: hidden;
    font-family: "Roboto", Arial, sans-serif;
  }
  .photo-area {
    position: absolute;
    inset: 0;
    background:
      radial-gradient(ellipse at 30% 45%, rgba(240,220,170,0.55) 0%, rgba(240,220,170,0) 45%),
      linear-gradient(180deg, var(--park-shade) 0%, #6d6a3a 30%, #8a7a45 45%, var(--park-green) 55%, #5f9a2a 75%, var(--autumn) 100%);
  }
  .shapes {
    position: absolute;
    inset: 0;
  }
  .brand {
    position: absolute;
    left: 590px;
    width: 570px;
    top: 24px;
    text-align: center;
    color: var(--white);
    font-family: "Roboto Condensed", Arial, sans-serif;
  }
  .brand-name {
    margin: 0;
    font-weight: 700;
    font-size: 56px;
    line-height: 70px;
  }
  .brand-tagline {
    margin: 12px 0 0;
    font-weight: 400;
    font-size: 40px;
    line-height: 52px;
  }
  .offer {
    position: absolute;
    inset: 0;
    margin: 0;
    color: var(--white);
    font-family: "Allura", cursive;
    font-size: 78px;
    font-weight: 400;
    line-height: 78px;
    text-shadow: 1px 1px 2px rgba(90,60,20,0.35);
  }
  .offer-line {
    position: absolute;
    right: 34px;
    white-space: nowrap;
  }
  .offer-line--1 { top: 306px; }
  .offer-line--2 { top: 378px; }
  .offer-line--3 { top: 478px; }
  .offer-line--4 { top: 558px; }
  .offer-amount {
    font-family: "Marcellus", serif;
    color: var(--brand-red);
    font-size: 74px;
    text-shadow: 1px 1px 1px rgba(90,60,20,0.3);
  }
  .fine-print {
    position: absolute;
    left: 520px;
    top: 675px;
    margin: 0;
    padding: 0;
    list-style: none;
    color: var(--text-red);
    font-size: 21.5px;
    line-height: 34px;
  }
  .fine-print li { padding-left: 18px; }
  .fine-print li:first-child { padding-left: 0; }
  .fine-print .wrap { display: inline-block; line-height: 30px; }
  .contact {
    position: absolute;
    left: 41px;
    top: 773px;
    color: var(--text-red);
    font-family: "Roboto", Arial, sans-serif;
    font-style: normal;
    font-size: 27px;
    line-height: 43px;
  }
  .contact p { margin: 0; }
  .contact strong { font-weight: 700; }
</style>
</head>
<body>
<main class="postcard">
  <div class="photo-area" role="img" aria-label="Photo of a dog leaping up on its hind legs in a sunny autumn park with falling leaves"></div>

  <svg class="shapes" width="1200" height="923" viewBox="0 0 1200 923" aria-hidden="true">
    <defs>
      <linearGradient id="gold-panel" x1="0" y1="0" x2="0" y2="1">
        <stop offset="0" stop-color="#d9c47c"/>
        <stop offset="0.5" stop-color="#c9ad62"/>
        <stop offset="1" stop-color="#a88a4a"/>
      </linearGradient>
      <linearGradient id="red-badge" x1="0" y1="0" x2="0" y2="1">
        <stop offset="0" stop-color="#d1121b"/>
        <stop offset="1" stop-color="#a60a10"/>
      </linearGradient>
      <linearGradient id="white-box" x1="0" y1="0" x2="0" y2="1">
        <stop offset="0" stop-color="#ffffff"/>
        <stop offset="1" stop-color="#e6e6e6"/>
      </linearGradient>
    </defs>

    <polygon points="290,757 1200,228 1200,923 290,923" fill="url(#gold-panel)"/>
    <polygon points="262,757 1200,210 1200,232 300,757" fill="#d1121b"/>
    <rect x="470" y="665" width="730" height="222" fill="#e9d98a"/>
    <polygon points="390,757 470,757 540,887 490,923" fill="#8a6f3a" opacity="0.6"/>
    <polygon points="0,757 390,757 490,923 0,923" fill="url(#white-box)"/>
    <rect x="470" y="885" width="730" height="38" fill="#d1121b"/>

    <circle cx="875" cy="8" r="292" fill="#d9d9d9"/>
    <circle cx="875" cy="0" r="286" fill="url(#red-badge)"/>
  </svg>

  <header class="brand">
    <h1 class="brand-name">Your Company<br>Name &amp; Logo Here</h1>
    <p class="brand-tagline">A Pet Resort</p>
  </header>

  <h2 class="offer">
    <span class="offer-line offer-line--1">New</span>
    <span class="offer-line offer-line--2">customers</span>
    <span class="offer-line offer-line--3">receive <span class="offer-amount">50%</span> off</span>
    <span class="offer-line offer-line--4">boarding*</span>
  </h2>

  <ul class="fine-print">
    <li>* 50% offer applies to standard lodging fees only.</li>
    <li>Amenities and playtimes not included in this offer.</li>
    <li>Valid for up to 10 nights of boarding.</li>
    <li><span class="wrap">Blackout dates of July 4th, Thanksgiving week and Christmas<br>week apply.</span></li>
    <li>Reservations required.</li>
  </ul>

  <address class="contact">
    <p>Contact For More Details :</p>
    <p><strong>000-000-0000</strong></p>
    <p>E-Mail : <strong>yourid@mail.com</strong></p>
  </address>
</main>
</body>
</html>
```